Children's martial arts flyer for new classes

Need a postcard flyer addressing the attached spec (see file).

Flyer needs to be Postcard Size and be suited in style to the target demographic which is parents of children aged 5-12 years old.

Classes are new.

Postcard must include the logo and a picture. I have included an example pic in the attached file, but feel free to use other suitable pics.

Target Market(s)

Parents with children aged 5-12 years old

Colors

Designer to choose colors to be used in the design.

Requirements
Must have
• clean look.
• professional.

```html
<!DOCTYPE html>
<html lang="en">
<head>
<meta charset="utf-8">
<title>Children's Martial Art Classes</title>
<link rel="stylesheet" href="https://fonts.googleapis.com/css2?family=Righteous&family=Open+Sans:ital,wght@0,400;0,600;0,700;1,400&display=swap">
<style>
  :root {
    --red: #e8131b;
    --ink: #111111;
    --paper: #ffffff;
    --photo-light: #ecebea;
    --photo-dark: #2e2e30;
    --map-fill: #e4e2de;
  }
  * { margin: 0; padding: 0; box-sizing: border-box; }
  html, body { width: 800px; height: 1200px; overflow: hidden; background: var(--paper); }
  .flyer {
    position: relative;
    width: 800px;
    height: 1200px;
    background: var(--paper);
    font-family: "Open Sans", Arial, sans-serif;
    color: var(--ink);
    overflow: hidden;
  }
  .headline {
    position: absolute;
    left: 30px;
    top: 40px;
    font-family: "Righteous", "Arial Black", sans-serif;
    font-weight: 400;
    font-size: 46px;
    line-height: 45px;
    letter-spacing: 1px;
    text-transform: uppercase;
    transform: scaleX(1.45);
    transform-origin: left top;
    white-space: nowrap;
  }
  .headline .red { color: var(--red); }
  .headline .dark { color: var(--ink); }
  .tagline {
    position: absolute;
    left: 30px;
    top: 196px;
    font-size: 28px;
    line-height: 38px;
  }
  .tagline .accent { color: var(--red); }
  .brand {
    position: absolute;
    right: 26px;
    top: 84px;
    display: flex;
    align-items: center;
    gap: 12px;
  }
  .brand-dot { width: 44px; height: 44px; border-radius: 50%; background: var(--red); }
  .brand-name { font-weight: 700; font-size: 26px; color: var(--ink); text-transform: uppercase; }
  .hero-photo {
    position: absolute;
    left: 170px;
    top: 276px;
    width: 300px;
    height: 680px;
    border-radius: 130px 130px 40px 40px;
    background: radial-gradient(ellipse at 50% 50%, var(--photo-dark) 0%, #4a4a4d 50%, var(--photo-light) 100%);
  }
  .schedule {
    position: absolute;
    left: 480px;
    top: 602px;
  }
  .schedule .days { font-size: 31px; font-style: italic; color: var(--ink); line-height: 40px; white-space: nowrap; }
  .schedule .days em { color: var(--red); }
  .schedule .days .amp { font-style: normal; }
  .schedule .time { font-size: 52px; font-weight: 700; color: var(--red); line-height: 62px; }
  .schedule .time span { font-size: 26px; font-weight: 400; color: var(--ink); }
  .schedule .address { font-size: 30px; line-height: 32px; margin-top: 4px; white-space: nowrap; }
  .location-map {
    position: absolute;
    left: 478px;
    top: 794px;
    width: 302px;
    height: 252px;
    border: 3px solid var(--ink);
    background: var(--paper);
    padding: 10px;
  }
  .location-map .map-area {
    width: 100%;
    height: 100%;
    background: var(--map-fill);
  }
  .booking {
    position: absolute;
    left: 20px;
    top: 976px;
  }
  .booking .call { font-size: 29px; line-height: 38px; }
  .booking .phone { font-size: 50px; font-weight: 700; color: var(--red); line-height: 58px; white-space: nowrap; }
  .booking .note { font-size: 28px; line-height: 36px; white-space: nowrap; }
  .web {
    position: absolute;
    left: 20px;
    top: 1158px;
    font-size: 26px;
    line-height: 34px;
  }
</style>
</head>
<body>
<main class="flyer">
  <h1 class="headline">
    <span class="red">Children's</span><br>
    <span class="dark">Martial Art</span><br>
    <span class="red">Classes</span>
  </h1>

  <div class="brand">
    <span class="brand-dot"></span>
    <span class="brand-name">Redline Kids</span>
  </div>

  <p class="tagline">
    <span class="accent">Fun</span> and <span class="accent">exciting</span> yet<br>
    <span class="accent">controlled</span> and <span class="accent">disciplined.</span>
  </p>

  <div class="hero-photo" role="img" aria-label="Photo of a child in a black silk martial arts uniform standing on one leg with arms outstretched"></div>

  <section class="schedule">
    <p class="days"><em>Tuesday’s</em> <span class="amp">&amp;</span> <em>Thursday’s</em></p>
    <p class="time">6pm <span>@</span></p>
    <p class="address">4/18 Harlow Street<br>Kensworth VIC 3099.</p>
  </section>

  <div class="location-map">
    <div class="map-area" role="img" aria-label="Street map showing the class location on Harlow Street"></div>
  </div>

  <section class="booking">
    <p class="call">Call</p>
    <p class="phone">0400 555 018</p>
    <p class="note">to book a free trial class.</p>
  </section>

  <p class="web">www.redlinekids.com.au</p>
</main>
</body>
</html>
```